Nine Lanterns Quill House Book Cover for: "Growing Older Wisely"

We are a publishing company who plans to launch the book, Growing Older Wisely, A Handy Compact Manual for Legal, Financial and Emotional Health in late 2018. We desire a book cover that creates interest, looks professional and can draw readers to open and purchase this book. Growing Older Wisely is an invaluable, self-help book which provides Generation X, Baby Boomers and their families with the following information: steps to obtain valid, reliable wills and trusts, identify and pay for health care, address end of life care and manage grief. (Please see the attached book description for more information about the book contents). The cover needs to have a "wellness", health and healing emphasis but it should not be morbid. Instead, the cover should have an uplifting, inviting and engaging feeling.

The designer should use Photoshop to develop the 5 x 7 cover. Please design the front, back cover and spine using the attached suggested layout as a guide. Use colors that complement the background colors in the author's photo and the logo for the front and back colors. Feel free to change the colors of the black rectangles on the front of the book. We are looking for a design to be added using the suggested layouts but we are open to modifications of the layout provided that all the content in the attachments are used. Below are the specifications needed for the cover:

-Use Photoshop
-Develop a front and back cover for a 5 x 7 format book
-Include the book title, subtitle and author name on the front cover as noted on the front cover attachment
-Include a book title and author names on the spine of the cover
-Use full bleed background if appropriate
-Color correct and resize images as necessary
-Insert logo and publisher’s imprint on spine and back cover as noted in attachments

For designers who are successful with this contest, we will primarily consider you for future projects.

Thanks!

Target Market(s)

Generation X, Baby Boomers and their families

Industry/Entity Type

Book Publisher

Font styles to use
Sans Serif

Colors

Designer to choose colors to be used in the design.

Requirements
Must have
• The designer should use Photoshop to develop the 5 x 7 cover. Please design the front, back cover and spine using the attached suggested layout as a guide. Use colors that complement the background colors in the author's photo and the logo for the front and back colors. Feel free to change the colors of the black rectangles on the front of the book. We are looking for a design to be added using the suggested layouts but we are open to modifications of the layout provided that all the content in the attachments are used. Below are the specifications needed for the cover:
• -Use Photoshop
• -Develop a front and back cover for a 5 x 7 format book
• -Include the book title, subtitle and author name on the front cover as noted on the front cover attachment
• -Include a book title and author names on the spine of the cover
• -Use full bleed background if appropriate
• -Color correct and resize images as necessary
• -Insert logo and publisher’s imprint on spine and back cover as noted in attachments
Nice to have
• N/A
Should not have
• The design should not specifically duplicate the layout samples or include pictures of persons on the cover. We have provided those as a guide; we are looking for innovation and professionalism.

```html
<!DOCTYPE html>
<html lang="en">
<head>
<meta charset="utf-8">
<title>Growing Older Wisely — Book Cover</title>
<link href="https://fonts.googleapis.com/css2?family=Bebas+Neue&family=Raleway:wght@400;700&display=swap" rel="stylesheet">
<style>
  :root {
    --backdrop: #a9a9a9;
    --paper: #ffffff;
    --navy: #27235f;
    --quote-brown: #6b4a3a;
    --quote-mark: #efe0d2;
    --ink: #1c1a2e;
    --sun-glow: #ffd27a;
    --sky-warm: #f2b98a;
    --sky-pale: #e9dccb;
    --dusk: #5c4a4a;
  }
  * { margin: 0; padding: 0; box-sizing: border-box; }
  html, body {
    width: 883px; height: 1200px; overflow: hidden;
    background: var(--backdrop);
  }
  .cover {
    position: absolute; left: 73px; top: 84px;
    width: 737px; height: 1032px;
    background: var(--paper);
    overflow: hidden;
  }
  .endorsement {
    position: absolute; left: 0; top: 0; width: 100%; height: 218px;
  }
  .quote-mark {
    position: absolute; top: 72px; width: 96px; height: 82px;
  }
  .quote-mark.open { left: 126px; }
  .quote-mark.close { left: 515px; }
  .endorsement-word {
    position: absolute; left: 0; width: 100%; top: 68px; text-align: center;
    font-family: "Raleway", sans-serif; font-weight: 700; font-size: 45px;
    color: var(--quote-brown); letter-spacing: -0.5px;
  }
  .endorsement-source {
    position: absolute; left: 0; width: 100%; top: 128px; text-align: center;
    font-family: "Raleway", sans-serif; font-weight: 400; font-size: 22px;
    color: var(--quote-brown);
  }
  .title-band {
    position: absolute; left: 0; top: 218px; width: 100%; height: 162px;
    background: var(--navy);
    display: flex; align-items: center; justify-content: center;
  }
  .book-title {
    font-family: "Bebas Neue", sans-serif; font-weight: 400; font-size: 98px;
    color: var(--paper); letter-spacing: 1px; line-height: 1; padding-top: 8px;
  }
  .hero-image {
    position: absolute; left: 0; top: 380px; width: 100%; height: 544px;
    background:
      radial-gradient(ellipse 260px 300px at 250px 370px, var(--sun-glow) 0%, rgba(255,210,122,0.6) 35%, rgba(242,185,138,0) 75%),
      linear-gradient(180deg, #b9b3ad 0%, var(--sky-pale) 30%, var(--sky-warm) 65%, #c98a6e 85%, var(--dusk) 100%);
  }
  .subtitle-box {
    position: absolute; left: 441px; top: 588px; width: 254px; height: 174px;
    background: rgba(255,255,255,0.92);
    display: flex; align-items: center; justify-content: center; text-align: center;
  }
  .subtitle {
    font-family: "Bebas Neue", sans-serif; font-size: 28px; line-height: 34px;
    color: var(--ink); letter-spacing: 0.3px;
  }
  .authors {
    position: absolute; left: 0; top: 924px; width: 100%; height: 108px;
    display: flex; align-items: center; justify-content: center;
    font-family: "Bebas Neue", sans-serif; font-size: 35px; color: var(--navy);
    letter-spacing: 0.4px; padding-top: 4px;
  }
</style>
</head>
<body>
  <main class="cover">
    <section class="endorsement">
      <svg class="quote-mark open" viewBox="0 0 96 82" aria-hidden="true">
        <polygon points="8,0 36,0 28,30 28,82 0,82 0,30" fill="var(--quote-mark)"/>
        <polygon points="64,0 92,0 84,30 84,82 56,82 56,30" fill="var(--quote-mark)"/>
      </svg>
      <svg class="quote-mark close" viewBox="0 0 96 82" aria-hidden="true">
        <polygon points="4,0 32,0 32,52 24,82 0,82 4,52" fill="var(--quote-mark)"/>
        <polygon points="62,0 90,0 90,52 82,82 58,82 62,52" fill="var(--quote-mark)"/>
      </svg>
      <p class="endorsement-word">Indispensable!</p>
      <p class="endorsement-source">--The Riverbend Courier</p>
    </section>

    <header class="title-band">
      <h1 class="book-title">GROWING OLDER WISELY</h1>
    </header>

    <div class="hero-image" role="img" aria-label="Photo of raised open hands reaching toward a glowing sunset sky as birds fly free"></div>

    <div class="subtitle-box">
      <p class="subtitle">A Handy<br>Compact Manual for<br>Legal, Financial and<br>Emotional Health</p>
    </div>

    <footer class="authors">Maren J. Holloway, M.P.A. with Theo R. Brandt, Esq.</footer>
  </main>
</body>
</html>
```